high-impact, conversion-focused website redesign for the government sector

Objective: To design and develop a high-impact, conversion-focused digital platform that solidifies Harrowfield Bright Associates (HBA) as the leading communications and strategy firm for government, defense, and industrial clients. The site must project authority, innovation, and sophisticated precision. See the creative breif for more information

Target Market(s)

Government contractors

Industry/Entity Type

Government, defense, industrials

Coding

Coded - Design and coding required

Number of Pages Required

5+ page

Font styles to use
Other font styles liked:
• See the current website

Requirements
Must have
• See design brief
Nice to have
• See design brief
Should not have
• See design brief

```html
<!DOCTYPE html>
<html lang="en">
<head>
<meta charset="utf-8">
<title>Meet Our Team – Harrowfield Bright Associates</title>
<link href="https://fonts.googleapis.com/css2?family=Lexend:wght@300;400;500;600&family=Russo+One&display=swap" rel="stylesheet">
<style>
:root{
  --navy:#0b1d3a;
  --navy-deep:#050f2a;
  --ink:#16233f;
  --text:#2b3550;
  --blue:#1f8ff0;
  --blue-bright:#2196f3;
  --green:#7ac142;
  --white:#ffffff;
  --rule:#d9dde4;
  --bar:#eef0f3;
}
*{margin:0;padding:0;box-sizing:border-box}
html,body{width:1200px;height:3008px;overflow:hidden}
body{position:relative;background:var(--white);font-family:'Lexend',sans-serif;color:var(--text)}
.display{font-family:'Russo One',sans-serif;letter-spacing:1px}

/* hero */
.hero{position:absolute;left:0;top:0;width:1200px;height:620px;
  background:radial-gradient(ellipse at 55% 45%,#2d4c72 0%,#1a3254 40%,#0c1d38 80%);}
.hero-shape{position:absolute;left:0;top:0}
.site-nav a{position:absolute;top:68px;color:var(--white);text-decoration:none;font-size:14px;font-weight:500}
.site-nav .active{border-bottom:1px solid var(--white);padding-bottom:6px}
.wordmark{position:absolute;text-align:center;font-family:'Lexend',sans-serif;font-weight:400;color:var(--white)}
.wordmark .name{font-size:19px;letter-spacing:0.5px;line-height:1}
.wordmark .sub{font-size:10px;letter-spacing:3px;margin-top:6px}
.btn-contact{position:absolute;left:906px;top:58px;width:166px;height:42px;color:var(--white);font-size:14px;font-weight:500;
  display:flex;align-items:center;justify-content:center;text-decoration:none}
.btn-contact svg{position:absolute;left:0;top:0}
.scroll-cue{position:absolute;left:34px;top:257px;width:2px;height:60px;background:var(--white)}
.scroll-text{position:absolute;left:27px;top:396px;transform:rotate(-90deg);transform-origin:left top;color:#c5cfdd;font-size:12px;line-height:14px;letter-spacing:2px;white-space:nowrap}
.eyebrow{position:absolute;left:0;width:1200px;top:198px;text-align:center;color:var(--white);font-size:22px}
.eyebrow::before,.eyebrow::after{content:"";display:inline-block;width:42px;height:2px;background:var(--white);vertical-align:middle;margin:0 14px}
.hero-title{position:absolute;left:0;width:1200px;top:234px;text-align:center;color:var(--white);font-size:42px;font-weight:400}

/* profile */
.portrait{position:absolute;left:128px;top:655px}
.profile-name{position:absolute;left:440px;top:666px;font-size:25px;font-weight:600;color:var(--ink)}
.profile-role{position:absolute;left:440px;top:710px;font-size:15.5px;color:var(--ink)}
.section-label{color:var(--blue-bright);font-weight:600;font-size:19px}
.expertise-title{position:absolute;left:440px;top:763px}
.expertise-list{position:absolute;left:440px;top:790px;width:650px;font-size:13.8px;line-height:23px;font-weight:300;color:var(--ink)}
.bio{position:absolute;left:141px;top:937px;width:975px;font-size:13.4px;line-height:19.4px;font-weight:300;color:var(--ink)}
.bio p{margin-bottom:19.5px}
.bio p.gap{margin-bottom:39px}
.accomplish-title{position:absolute;left:141px;top:1622px}
.accomplish{position:absolute;left:141px;top:1662px;width:940px;list-style:none;font-size:13.8px;font-weight:300;color:var(--ink);line-height:23px}
.accomplish li{position:relative;padding-left:23px;margin-bottom:8px}
.accomplish li::before{content:"";position:absolute;left:3px;top:7px;width:7px;height:7px;border-top:2px solid var(--blue-bright);border-right:2px solid var(--blue-bright);transform:rotate(45deg)}

/* contact band */
.contact-band{position:absolute;left:0;top:1955px;width:1200px;height:705px;
  background:radial-gradient(ellipse at 50% 95%,#1b4a9a 0%,#0c2458 35%,var(--navy-deep) 70%)}
.contact-band svg{position:absolute;left:0;top:0}
.divider-line{position:absolute;left:616px;top:2067px;width:2px;height:66px;background:var(--green)}
.contact-eyebrow{position:absolute;left:0;width:1220px;top:2172px;text-align:center;color:var(--blue-bright);font-size:16px;letter-spacing:4px;font-weight:500}
.contact-title{position:absolute;left:0;width:1220px;top:2199px;text-align:center;color:var(--white);font-size:38px;font-weight:400}
.contact-copy{position:absolute;left:150px;width:920px;top:2277px;text-align:center;color:var(--white);font-size:18.5px;line-height:27.5px;font-weight:400}
.btn-learn{position:absolute;left:503px;top:2394px;width:236px;height:54px;color:var(--white);font-size:19px;font-weight:500;display:flex;align-items:center;justify-content:center;text-decoration:none}
.btn-learn svg{position:absolute;left:0;top:0}
.btn-learn span{position:relative}

/* footer */
.footer-mark{color:var(--navy)}
.footer-rule{position:absolute;left:113px;width:964px;height:1px;background:var(--rule)}
.footer-nav{position:absolute;left:113px;top:2772px;width:964px;display:flex;justify-content:center;align-items:center}
.footer-nav a{color:var(--ink);text-decoration:none;font-size:17px;font-weight:400}
.footer-nav .dot{width:5px;height:5px;background:var(--green);margin:0 40px}
.contact-item{position:absolute;top:2848px;display:flex;align-items:center;gap:14px}
.contact-item .label{color:var(--blue-bright);font-size:13px;display:block}
.contact-item .value{color:var(--ink);font-size:13px;line-height:17px}
.copyright-bar{position:absolute;left:0;top:2951px;width:1200px;height:57px;background:var(--bar);font-size:12px;color:var(--ink)}
.copyright-bar .left{position:absolute;left:183px;top:22px}
.copyright-bar .right{position:absolute;right:124px;top:21px;display:flex;gap:16px}
</style>
</head>
<body>

<!-- hero -->
<section class="hero" role="img" aria-label="Photo of a team collaborating around a desk in a dim blue-lit office"></section>
<svg class="hero-shape" width="1200" height="620" viewBox="0 0 1200 620" aria-hidden="true">
  <polygon points="0,584 600,478 1200,584 1200,620 0,620" fill="#2196f3"/>
  <polygon points="0,606 600,494 1200,606 1200,620 0,620" fill="#ffffff"/>
</svg>

<nav class="site-nav">
  <a style="left:85px">HOME</a>
  <a style="left:165px">ADVISORY SERVICES</a>
  <a class="active" style="left:345px">ABOUT US</a>
  <a style="left:781px">BLOG</a>
</nav>
<div class="wordmark" style="left:450px;top:58px;width:300px">
  <div class="name">HARROWFIELD BRIGHT</div>
  <div class="sub">ASSOCIATES</div>
</div>
<a class="btn-contact">
  <svg width="166" height="42" viewBox="0 0 166 42"><polygon points="12,1 154,1 165,21 154,41 12,41 1,21" fill="none" stroke="#fff" stroke-width="2"/></svg>
  <span style="position:relative">CONTACT US ↗</span>
</a>
<div class="scroll-cue"></div>
<div class="scroll-text">SCROLL</div>
<div class="eyebrow display">OUR EXPERTS</div>
<h1 class="hero-title display">MEET OUR TEAM</h1>

<!-- profile -->
<svg class="portrait" width="277" height="242" viewBox="0 0 277 242" role="img" aria-label="Portrait photo of Dana Whitmore">
  <defs><linearGradient id="portraitFill" x1="0" y1="0" x2="0" y2="1"><stop offset="0" stop-color="#5b6f8e"/><stop offset="1" stop-color="#1f3564"/></linearGradient></defs>
  <polygon points="1,121 70,1 207,1 276,121 207,241 70,241" fill="none" stroke="#2196f3" stroke-width="2"/>
  <polygon points="11,121 76,10 201,10 266,121 201,232 76,232" fill="url(#portraitFill)"/>
</svg>
<h2 class="profile-name">Dana Whitmore</h2>
<div class="profile-role">Communications, Investor Relations, &amp; Marketing Strategist | Board Advisor</div>
<div class="section-label expertise-title">Industry Expertise</div>
<div class="expertise-list">Financial Services | Defense | Cybersecurity | Maritime | Energy | Foreign and Domestic Government Affairs | Real Estate | Financial Technology | Blockchain | Artificial Intelligence and Machine Learning</div>

<div class="bio">
  <p>Dana Whitmore, founder and principal of Harrowfield Bright Associates, is an award-winning global communications and investor relations strategist with decades of experience building, scaling, and protecting global public and private brands.</p>
  <p class="gap">Dana takes a data-driven approach to marketing and communications. Clients she has worked with have raised billions in capital, scaled from start-up to nine-figure exits, built and scaled cutting-edge technologies, executed profitable M&amp;As, built and scaled international sales and distribution channels, closed major customers, and, most importantly, created massive shareholder value.</p>
  <p>Dana founded and sold technology-focused strategic marketing and communications firm Northgate PR. Areas of expertise included cybersecurity, IOT, hardware, blockchain, PropTech, InvestTech, banking, artificial intelligence, and many other highly technical areas. She additionally advised the foreign economic ministries of two nations on how to raise their global profile and was the agency of record for Summit Forward’s Accelerator. The firm also served numerous financial services firms, significantly increasing AUM.</p>
  <p>A skilled technologist, Dana brings vast experience educating customers, the media, and investors about the applicability of new technology. She has devised strategies that educated global markets on blockchain’s applicability outside of digital currency, worked across hardware IOT and financial cybersecurity technologies, and worked extensively within the artificial intelligence space across robotics and process automation.</p>
  <p>As an investor relations professional, Dana sat on the investment committee at Meridian Holdings, evaluating middle market companies across cybersecurity, defense, maritime, and engineering technology, among other areas. She served as the Chief Strategy Officer for Talvern Capital. There, she built and led the investor relations team, responsible for raising capital for direct investments ranging from $1B to $80M. Additionally, she was responsible for building an award-winning, tech-enabled, public non-traded REIT, Crestline Avenue. Built at a fraction of the cost of competitors, it won CREs’ best new online capital raising platform and created successful acquisition channels for retail, RIA, and institutional investors. Dana previously served as Director of Acquisitions for Oakridge Property Group, underwriting and acquiring $250M in real estate, helping to grow the firm from 4 to 75 employees and making the “Growth 5000” list twice.</p>
  <p>A pioneer within the online investing space, Dana sat on the board of CFOA for six years, working with national securities regulators on crowdfunding rule implementation, enabling online investing as we know it today.</p>
  <p>She is an advisor and mentor to numerous industry boards. Past and current board positions include Summit Forward &amp; Elder Forum Accelerator, Digital Finance Guild, and CFOA.</p>
  <p>Dana, a sought-after speaker and media contributor won numerous awards, including Women in Media Council’ “Outstanding Communicators,” Executive Review Magazine’s “Entrepreneur of the Year,” and the Capital City Under 40 Award. Dana served as a National Reserve and State Guard officer.</p>
</div>

<div class="section-label accomplish-title">Career Accomplishments</div>
<ul class="accomplish">
  <li>Firms Dana worked with have raised billions in capital</li>
  <li>Gone from start-up to exit</li>
  <li>Built and scaled cutting-edge technologies</li>
  <li>Executed profitable M&amp;A strategies</li>
  <li>Built and scaled international sales and distribution channels</li>
  <li>Closed major customers, and created massive shareholder value</li>
  <li>She built and scaled Crestline Avenue, an award-winning, tech-enabled, Public Non-traded REIT that won CRE’s best new online capital raising platform and created successful acquisition channels for retail, RIAs, and institutional investors. Dana founded and sold a leading technology-focused strategic communications and marketing firm, Northgate PR.</li>
</ul>

<!-- contact band -->
<section class="contact-band" role="img" aria-label="Background image of a glowing blue digital network over the Earth">
  <svg width="1200" height="705" viewBox="0 0 1200 705" aria-hidden="true">
    <polygon points="0,0 1200,0 1200,5 600,138 0,5" fill="#ffffff"/>
    <polygon points="0,5 600,138 1200,5 1200,28 600,146 0,28" fill="#2196f3"/>
    <polygon points="0,650 600,555 1200,650 1200,705 0,705" fill="#2196f3"/>
    <polygon points="0,673 600,563 1200,673 1200,705 0,705" fill="#ffffff"/>
  </svg>
</section>
<div class="divider-line"></div>
<div class="contact-eyebrow">CONTACT US</div>
<h2 class="contact-title display">GET IN TOUCH WITH US</h2>
<p class="contact-copy">We help aerospace and defense leaders solve problems and achieve their goals, ensuring they excel at their business of changing the world. Connect with us today to learn how our team of communication, marketing, and event management experts can take your brand to the next level.</p>
<a class="btn-learn">
  <svg width="236" height="54" viewBox="0 0 236 54"><polygon points="14,0 222,0 236,27 222,54 14,54 0,27" fill="#2196f3"/></svg>
  <span>LEARN MORE ↗</span>
</a>

<!-- footer -->
<div class="wordmark footer-mark" style="left:450px;top:2660px;width:330px">
  <div class="name" style="font-size:24px">HARROWFIELD BRIGHT</div>
  <div class="sub" style="font-size:12px">ASSOCIATES</div>
</div>
<div class="footer-rule" style="top:2747px"></div>
<nav class="footer-nav">
  <a>HOME</a><span class="dot"></span>
  <a>ADVISORY SERVICES</a><span class="dot"></span>
  <a>ABOUT US</a><span class="dot"></span>
  <a>BLOG</a><span class="dot"></span>
  <a>CONTACT US</a>
</nav>
<div class="footer-rule" style="top:2825px"></div>

<div class="contact-item" style="left:193px">
  <svg width="50" height="46" viewBox="0 0 50 46" aria-hidden="true">
    <polygon points="0,23 12,0 38,0 50,23 38,46 12,46" fill="#7ac142"/>
    <path d="M25 11a8 8 0 0 0-8 8c0 6 8 15 8 15s8-9 8-15a8 8 0 0 0-8-8zm0 11a3 3 0 1 1 0-6 3 3 0 0 1 0 6z" fill="#fff"/>
  </svg>
  <div><span class="label">Location</span><div class="value">418 Linden Ave Suite 300<br>Austin TX, 78702</div></div>
</div>
<div class="contact-item" style="left:528px">
  <svg width="50" height="46" viewBox="0 0 50 46" aria-hidden="true"><polygon points="0,23 12,0 38,0 50,23 38,46 12,46" fill="#7ac142"/></svg>
  <div><span class="label">Network</span><div class="value" style="font-size:15px">harrowfield-bright-associates</div></div>
</div>
<div class="contact-item" style="left:823px">
  <svg width="50" height="46" viewBox="0 0 50 46" aria-hidden="true">
    <polygon points="0,23 12,0 38,0 50,23 38,46 12,46" fill="#7ac142"/>
    <rect x="16" y="16" width="18" height="13" fill="#fff"/>
    <path d="M16 16l9 7 9-7" fill="none" stroke="#7ac142" stroke-width="1.6"/>
  </svg>
  <div><span class="label">Email us</span><div class="value">info@harrowfieldbright.partners</div></div>
</div>

<div class="copyright-bar">
  <span class="left">Copyright © 2025 Harrowfield Bright Associates</span>
  <span class="right"><span>Terms of Use</span><span>Privacy Policy</span></span>
</div>

</body>
</html>
```